Solids Control Presentation Template Design

I'm putting together a technical 5-day course about solids control and waste management. I'm looking for an updated art and a easy on the eyes format.

```html
<!DOCTYPE html>
<html lang="en">
<head>
<meta charset="utf-8">
<title>Solids Control Presentation Template</title>
<link href="https://fonts.googleapis.com/css2?family=Poppins:wght@400;500;600;700;800&display=swap" rel="stylesheet">
<style>
:root{
  --red:#9d2a30;
  --red-bright:#c0262d;
  --dark:#1e1a1b;
  --ink:#2a2a2a;
  --muted:#8a8a8a;
  --line:#e6e6e6;
  --white:#ffffff;
  --stage:#000000;
}
*{margin:0;padding:0;box-sizing:border-box}
html,body{width:1200px;height:1042px;overflow:hidden;background:var(--stage)}
body{font-family:'Poppins',sans-serif;color:var(--ink);position:relative}
.slide{position:absolute;width:586px;height:330px;background:var(--white);overflow:hidden}
.s1{left:13px;top:14px;background:var(--red)}
.s2{left:606px;top:14px}
.s3{left:13px;top:353px}
.s4{left:606px;top:353px}
.s5{left:13px;top:698px}
.s6{left:606px;top:698px}
.abs{position:absolute}
.photo{position:absolute}

/* brand mark */
.brand{position:absolute;right:8px;top:8px;width:116px;text-align:center;white-space:nowrap}
.brand-name{font-weight:800;font-size:14px;letter-spacing:1.4px;color:var(--dark);line-height:1}
.brand-tag{font-size:4.6px;letter-spacing:.9px;color:var(--red);text-transform:uppercase;margin-top:2px;line-height:1;white-space:nowrap}
.brand-sub{font-size:3.2px;letter-spacing:.2px;color:var(--dark);margin-top:1.5px;line-height:1;white-space:nowrap}

/* footers */
.footer{position:absolute;left:0;bottom:0;width:100%;height:20px;background:var(--red)}
.footer-end{position:absolute;right:0;bottom:0;height:20px;width:112px;background:var(--dark);clip-path:polygon(0 0,100% 0,100% 100%,18px 100%)}
.footer-end span{position:absolute;right:30px;top:5px;font-size:8px;font-weight:700;color:var(--white);white-space:nowrap}
.copyright{position:absolute;left:8px;top:5px;font-size:8px;font-weight:700;color:var(--white)}

/* text */
.lorem{font-size:5.2px;line-height:9.5px;color:var(--muted)}
.item-title{font-size:7.5px;font-weight:600;color:var(--ink);line-height:1.2}
.badge{position:absolute;width:20px;height:20px;background:var(--red);color:var(--white);font-size:8px;font-weight:700;display:flex;align-items:center;justify-content:center;clip-path:polygon(50% 0,100% 25%,100% 75%,50% 100%,0 75%,0 25%)}

/* slide 1 */
.cover-title{position:absolute;right:16px;top:104px;width:330px;text-align:right;color:var(--white);font-weight:800;font-size:30px;line-height:41px}
.cover-sub{position:absolute;right:14px;top:192px;width:330px;text-align:right;color:var(--white);font-weight:700;font-size:11.5px;padding:4px 0;border-top:1px solid rgba(255,255,255,.15);border-bottom:1px solid rgba(255,255,255,.15)}
.cover-brand{position:absolute;right:16px;top:236px;width:250px;text-align:center;color:var(--white);white-space:nowrap}
.cover-brand .brand-name{color:var(--white);font-size:30px;letter-spacing:4px}
.cover-brand .brand-tag{color:var(--white);font-size:10px;letter-spacing:3px;margin-top:3px}
.cover-brand .brand-sub{color:var(--white);font-size:6.4px;letter-spacing:1.4px;margin-top:4px}

/* slide 2 */
.section-title{font-weight:700;color:var(--dark);letter-spacing:-.2px;white-space:nowrap}
.section-title em{font-style:normal;color:var(--red)}
.service{position:absolute;width:130px;height:100px;border:1px solid var(--line);border-radius:4px 22px 4px 22px;text-align:center;box-shadow:0 2px 6px rgba(0,0,0,.04)}
.service .badge{left:55px;top:10px;width:20px;height:20px;clip-path:none;border-radius:4px}
.service .item-title{position:absolute;left:0;right:0;top:44px;font-size:7px;font-weight:500}
.service .lorem{position:absolute;left:8px;right:8px;top:56px;font-size:4.8px;line-height:9.5px}

/* slide 3 & 6 lists */
.list-item{position:absolute}
.list-item .item-title{position:absolute;left:0;top:0;white-space:nowrap}
.list-item .lorem{position:absolute;left:0;top:11px;width:175px}

/* slide 4 banners */
.banner{position:absolute;width:230px;height:58px;color:var(--white);padding:13px 22px 0 24px}
.banner.red{background:var(--red);clip-path:polygon(6% 0,100% 0,93% 50%,100% 100%,6% 100%,0 50%)}
.banner.dark{background:var(--dark);clip-path:polygon(0 0,94% 0,100% 50%,94% 100%,0 100%,6% 50%)}
.banner h4{font-size:7.2px;font-weight:600;margin-bottom:3px;white-space:nowrap}
.banner p{font-size:5px;line-height:10px;color:rgba(255,255,255,.85)}

/* slide 5 hexes */
.client{font-weight:600;color:var(--ink);font-size:10px;text-align:center;line-height:1.15;white-space:nowrap}
</style>
</head>
<body>

<!-- Slide 1: cover -->
<section class="slide s1">
  <svg class="photo" width="586" height="330" viewBox="0 0 586 330" role="img" aria-label="Photo of oil pumpjacks silhouetted against a red-tinted sunset sky">
    <defs>
      <linearGradient id="sky" x1="0" y1="0" x2="0" y2="1">
        <stop offset="0" stop-color="#7d1c22"/>
        <stop offset=".45" stop-color="#d98a8c"/>
        <stop offset=".7" stop-color="#8e3036"/>
        <stop offset="1" stop-color="#2b1214"/>
      </linearGradient>
    </defs>
    <polygon points="0,0 220,0 325,330 0,330" fill="url(#sky)"/>
  </svg>
  <svg class="abs" width="586" height="330" viewBox="0 0 586 330" style="left:0;top:0">
    <polygon points="258,146 270,146 342,330 330,330" fill="#3a3536"/>
    <polygon points="0,180 26,330 0,330" fill="#c0262d"/>
  </svg>
  <h1 class="cover-title">RESULTS DRIVEN<br>SOLIDS CONTROL</h1>
  <p class="cover-sub">RUNNING THE BACKYARD BY THE NUMBERS</p>
  <div class="cover-brand">
    <div class="brand-name">GRITLINE</div>
    <div class="brand-tag">Precision Field Solutions</div>
    <div class="brand-sub">ENGINEERING • CONSULTING • TRAINING • EQUIPMENT</div>
  </div>
</section>

<!-- Slide 2: engineering services -->
<section class="slide s2">
  <div class="brand"><div class="brand-name">GRITLINE</div><div class="brand-tag">Precision Field Solutions</div><div class="brand-sub">ENGINEERING • CONSULTING • TRAINING • EQUIPMENT</div></div>
  <h2 class="section-title abs" style="left:0;right:0;top:32px;text-align:center;font-size:21px">OUR <em>ENGINEERING</em> SERVICES</h2>

  <div class="service" style="left:90px;top:80px"><div class="badge">01</div><div class="item-title">Services - 01</div><p class="lorem">Lorem ipsum dolor sit amet, consectetur adipiscing elit, sed do eiusmod tempor incididunt ut labor aliqua.</p></div>
  <div class="service" style="left:228px;top:80px"><div class="badge">02</div><div class="item-title">Services - 02</div><p class="lorem">Lorem ipsum dolor sit amet, consectetur adipiscing elit, sed do eiusmod tempor incididunt ut labor aliqua.</p></div>
  <div class="service" style="left:367px;top:80px"><div class="badge">03</div><div class="item-title">Services - 03</div><p class="lorem">Lorem ipsum dolor sit amet, consectetur adipiscing elit, sed do eiusmod tempor incididunt ut labor aliqua.</p></div>
  <div class="service" style="left:90px;top:188px"><div class="badge">04</div><div class="item-title">Services - 04</div><p class="lorem">Lorem ipsum dolor sit amet, consectetur adipiscing elit, sed do eiusmod tempor incididunt ut labor aliqua.</p></div>
  <div class="service" style="left:228px;top:188px"><div class="badge">05</div><div class="item-title">Services - 05</div><p class="lorem">Lorem ipsum dolor sit amet, consectetur adipiscing elit, sed do eiusmod tempor incididunt ut labor aliqua.</p></div>
  <div class="service" style="left:367px;top:188px"><div class="badge">06</div><div class="item-title">Services - 06</div><p class="lorem">Lorem ipsum dolor sit amet, consectetur adipiscing elit, sed do eiusmod tempor incididunt ut labor aliqua.</p></div>

  <div class="footer"></div>
  <div class="footer-end" style="width:112px"><span>PAGE : 01</span></div>
</section>

<!-- Slide 3: training courses -->
<section class="slide s3">
  <svg class="photo" width="586" height="330" viewBox="0 0 586 330" role="img" aria-label="Photo of a hand writing notes beside a laptop, in a grey-teal tint" style="left:0;top:0">
    <defs>
      <linearGradient id="desk" x1="0" y1="0" x2="1" y2="1">
        <stop offset="0" stop-color="#5c6766"/>
        <stop offset=".55" stop-color="#7d8887"/>
        <stop offset="1" stop-color="#c5cccb"/>
      </linearGradient>
    </defs>
    <polygon points="0,0 325,0 225,330 0,330" fill="url(#desk)"/>
  </svg>
  <svg class="abs" width="586" height="330" viewBox="0 0 586 330" style="left:0;top:0">
    <polygon points="285,145 300,145 244,330 227,330" fill="#9d2a30"/>
    <polygon points="586,180 586,330 540,330" fill="#c0262d"/>
    <polygon points="586,240 586,330 560,330" fill="#9d2a30"/>
  </svg>
  <div class="brand"><div class="brand-name">GRITLINE</div><div class="brand-tag">Precision Field Solutions</div><div class="brand-sub">ENGINEERING • CONSULTING • TRAINING • EQUIPMENT</div></div>

  <h2 class="abs" style="left:323px;top:80px;font-size:14px;font-weight:700;color:var(--red);white-space:nowrap">OUR TRAINING COURSES</h2>
  <p class="lorem abs" style="left:323px;top:102px;width:210px">Lorem ipsum dolor sit amet, consectetur adipi scing elit, sed do eiusmod tempor incididunt ut labore et dolore magna aliqua.</p>

  <div class="badge" style="left:323px;top:135px;width:22px;height:24px"><svg width="10" height="10" viewBox="0 0 10 10"><circle cx="3" cy="5" r="2" fill="none" stroke="#fff" stroke-width=".9"/><circle cx="7" cy="3" r="1.6" fill="none" stroke="#fff" stroke-width=".9"/><circle cx="7" cy="7.5" r="1.4" fill="none" stroke="#fff" stroke-width=".9"/></svg></div>
  <div class="list-item" style="left:355px;top:136px"><div class="item-title">Solids Control for Drilling Engineers</div><p class="lorem">Lorem ipsum dolor sit amet, consectetur adipiscing elit, sed do eiusmod tempor incididunt ut labor aliqua.</p></div>

  <div class="badge" style="left:326px;top:184px;width:22px;height:24px"><svg width="10" height="10" viewBox="0 0 10 10"><circle cx="5" cy="4" r="2.6" fill="none" stroke="#fff" stroke-width=".9"/><path d="M3 6 L2 9.5 L5 8 L8 9.5 L7 6" fill="none" stroke="#fff" stroke-width=".9"/></svg></div>
  <div class="list-item" style="left:357px;top:179px"><div class="item-title">Drilling Waste Handling and Treatment</div><p class="lorem">Ipsum dolor sit amet, consectetur adipiscing elit, sed do eiusmod tempor incididunt ut labor aliqua.</p></div>

  <div class="badge" style="left:327px;top:227px;width:22px;height:24px"><svg width="10" height="10" viewBox="0 0 10 10"><circle cx="2.5" cy="5" r="1.4" fill="#fff"/><circle cx="7.5" cy="2.5" r="1.4" fill="#fff"/><circle cx="7.5" cy="7.5" r="1.4" fill="#fff"/><path d="M2.5 5 L7.5 2.5 M2.5 5 L7.5 7.5" stroke="#fff" stroke-width=".8"/></svg></div>
  <div class="list-item" style="left:358px;top:226px"><div class="item-title">Water Treatment</div><p class="lorem">Dolor sit amet, consectetur adipiscing elit, sed do eiusmod tempor incididunt ut labor aliqua.</p></div>

  <div class="badge" style="left:327px;top:272px;width:22px;height:24px"><svg width="10" height="10" viewBox="0 0 10 10"><rect x="1.5" y="3" width="7" height="5.5" fill="none" stroke="#fff" stroke-width=".9"/><rect x="3.5" y="1" width="3" height="2" fill="none" stroke="#fff" stroke-width=".9"/></svg></div>
  <div class="list-item" style="left:358px;top:272px"><div class="item-title">Solids Control for the Sales Team</div><p class="lorem">Dolor sit amet, consectetur adipiscing elit, sed do eiusmod tempor incididunt ut labor aliqua.</p></div>
</section>

<!-- Slide 4: approach -->
<section class="slide s4">
  <svg class="photo" width="218" height="330" viewBox="0 0 218 330" role="img" aria-label="Photo of two workers in hard hats shaking hands, silhouetted against a blue evening sky" style="left:0;top:0">
    <defs>
      <linearGradient id="dusk" x1="0" y1="0" x2="0" y2="1">
        <stop offset="0" stop-color="#5d7fa6"/>
        <stop offset=".55" stop-color="#b6c3cf"/>
        <stop offset=".8" stop-color="#d9c7a6"/>
        <stop offset="1" stop-color="#1a1a1a"/>
      </linearGradient>
    </defs>
    <rect width="218" height="330" fill="url(#dusk)"/>
  </svg>
  <div class="brand"><div class="brand-name">GRITLINE</div><div class="brand-tag">Precision Field Solutions</div><div class="brand-sub">ENGINEERING • CONSULTING • TRAINING • EQUIPMENT</div></div>

  <svg class="abs" width="586" height="330" viewBox="0 0 586 330" style="left:0;top:0">
    <path d="M283 88 H229 V238 H283" fill="none" stroke="#cfcfcf" stroke-width=".8"/>
    <line x1="277" y1="163" x2="440" y2="163" stroke="#cfcfcf" stroke-width=".8"/>
    <circle cx="283" cy="88" r="1.5" fill="#bdbdbd"/>
    <circle cx="283" cy="238" r="1.5" fill="#bdbdbd"/>
    <circle cx="440" cy="163" r="1.5" fill="#bdbdbd"/>
    <path d="M229 111 A52 52 0 0 0 229 215" fill="none" stroke="#9d2a30" stroke-width="3"/>
    <circle cx="229" cy="163" r="47" fill="#ffffff" stroke="#dddddd" stroke-width="1"/>
    <circle cx="229" cy="163" r="38" fill="#ffffff" stroke="#d0d0d0" stroke-width="6"/>
    <g fill="none" stroke="#c0262d" stroke-width="1.2" stroke-linecap="round">
      <path d="M223 167 C219 163 219 154 224 150 C228 147 234 148 236 152 C239 157 237 163 234 167 Z"/>
      <path d="M224 170 H234 M225 173 H233 M227 176 H231"/>
      <path d="M229 142 V139 M218 146 L216 144 M240 146 L242 144 M214 157 H211 M244 157 H247"/>
    </g>
  </svg>

  <div class="banner red" style="left:292px;top:59px"><h4>Business Market Research</h4><p>Lorem ipsum dolor sit amet, consectetur adipiscing elit, sed do eiusmod tempor incididunt ut labor aliqua.</p></div>
  <div class="banner dark" style="left:322px;top:135px;padding-left:20px"><h4>Finding Creative Solutions</h4><p>Lorem ipsum dolor sit amet, consectetur adipiscing elit, sed do eiusmod tempor incididunt ut labor aliqua.</p></div>
  <div class="banner red" style="left:292px;top:212px"><h4>Solving Problem With Confident</h4><p>Lorem ipsum dolor sit amet, consectetur adipiscing elit, sed do eiusmod tempor incididunt ut labor aliqua.</p></div>

  <div class="footer-end" style="height:22px;width:96px"><span style="top:6px;right:12px">PAGE : 01</span></div>
</section>

<!-- Slide 5: clients -->
<section class="slide s5">
  <div class="brand"><div class="brand-name">GRITLINE</div><div class="brand-tag">Precision Field Solutions</div><div class="brand-sub">ENGINEERING • CONSULTING • TRAINING • EQUIPMENT</div></div>
  <h2 class="abs" style="left:38px;top:43px;font-size:21px;font-weight:700;color:var(--red);white-space:nowrap">OUR CLIENTS</h2>
  <p class="abs" style="left:38px;top:76px;width:270px;font-size:7.3px;line-height:13.5px;color:var(--muted)">Lorem ipsum dolor sit amet, consectetur adipi scing elit, sed do eiusmod tempor incididunt ut labore et dolore magna aliqua.</p>

  <div class="badge" style="left:38px;top:124px;width:22px;height:24px">01</div>
  <div class="list-item" style="left:68px;top:122px"><div class="item-title" style="font-size:9.5px;font-weight:500">Experience</div><p class="lorem" style="top:14px;width:170px">Lorem ipsum dolor sit amet, consectetur adipiscing elit, sed do eiusmod tempor incididunt ut labor aliqua.</p></div>
  <div class="badge" style="left:38px;top:173px;width:22px;height:24px">02</div>
  <div class="list-item" style="left:68px;top:172px"><div class="item-title" style="font-size:9.5px;font-weight:500">Excellence</div><p class="lorem" style="top:14px;width:170px">Ipsum dolor sit amet, consectetur adipiscing elit, sed do eiusmod tempor incididunt ut labor aliqua.</p></div>
  <div class="badge" style="left:38px;top:223px;width:22px;height:24px">03</div>
  <div class="list-item" style="left:68px;top:221px"><div class="item-title" style="font-size:9.5px;font-weight:500">Effective</div><p class="lorem" style="top:14px;width:170px">Dolor sit amet, consectetur adipiscing elit, sed do eiusmod tempor incididunt ut labor aliqua.</p></div>

  <svg class="abs" width="586" height="330" viewBox="0 0 586 330" style="left:0;top:0">
    <g fill="#ffffff" stroke="#d8d8d8" stroke-width="1">
      <polygon points="372,34 418,59 418,109 372,134 326,109 326,59"/>
      <polygon points="465,34 511,59 511,109 465,134 419,109 419,59"/>
      <polygon points="326,116 372,141 372,191 326,216 280,191 280,141"/>
      <polygon points="419,116 465,141 465,191 419,216 373,191 373,141"/>
      <polygon points="511,116 557,141 557,191 511,216 465,191 465,141"/>
      <polygon points="372,196 418,221 418,271 372,296 326,271 326,221"/>
      <polygon points="465,196 511,221 511,271 465,296 419,271 419,221"/>
    </g>
  </svg>
  <div class="client abs" style="left:330px;top:77px;width:84px">Ridgeway Oil</div>
  <div class="client abs" style="left:423px;top:77px;width:84px">Halden Works</div>
  <div class="client abs" style="left:284px;top:159px;width:84px">Norvel</div>
  <div class="client abs" style="left:377px;top:159px;width:84px">Cresta Energy</div>
  <div class="client abs" style="left:469px;top:159px;width:84px">Petrova</div>
  <div class="client abs" style="left:330px;top:239px;width:84px">Sable Crest</div>
  <div class="client abs" style="left:423px;top:239px;width:84px">Albion Gas</div>

  <div class="footer"><span class="copyright">COPYRIGHT TEXT HERE</span></div>
  <div class="footer-end" style="width:112px"><span style="font-weight:400;right:14px">Page : 01</span></div>
</section>

<!-- Slide 6: progress -->
<section class="slide s6">
  <div class="photo" role="img" aria-label="Photo of drilling cuttings and mud on a shaker screen" style="left:0;top:0;width:122px;height:154px;background:linear-gradient(160deg,#6f675c,#a89a84 50%,#4a443d)"></div>
  <div class="photo" role="img" aria-label="Photo of a worker in a hard hat and gloves inspecting a screen" style="left:126px;top:16px;width:121px;height:155px;background:linear-gradient(170deg,#3f4a40,#8f8a7c 55%,#6b3a2c)"></div>
  <div class="photo" role="img" aria-label="Photo of a muddy waste pit with equipment" style="left:0;top:156px;width:122px;height:154px;background:linear-gradient(180deg,#5a5149,#8a7766 45%,#4b3b31)"></div>
  <div class="photo" role="img" aria-label="Photo of a modern office building under a blue and pink sky" style="left:126px;top:175px;width:121px;height:135px;background:linear-gradient(180deg,#5e7ab8,#c9a7c2 50%,#6f7f88 80%,#4f6b3c)"></div>

  <div class="brand"><div class="brand-name">GRITLINE</div><div class="brand-tag">Precision Field Solutions</div><div class="brand-sub">ENGINEERING • CONSULTING • TRAINING • EQUIPMENT</div></div>
  <h2 class="section-title abs" style="left:293px;top:47px;font-size:14px">HOW WE TRACK <em>OUR PROGRESS</em></h2>
  <p class="lorem abs" style="left:293px;top:69px;width:210px">Lorem ipsum dolor sit amet, consectetur adipi scing elit, sed do eiusmod tempor incididunt ut labore et dolore magna aliqua.</p>

  <div class="badge" style="left:293px;top:103px;width:22px;height:24px">01</div>
  <div class="list-item" style="left:325px;top:104px"><div class="item-title">Break out large tasks into smaller pieces</div><p class="lorem">Lorem ipsum dolor sit amet, consectetur adipiscing elit, sed do eiusmod tempor incididunt ut labor aliqua.</p></div>
  <div class="badge" style="left:293px;top:149px;width:22px;height:24px">02</div>
  <div class="list-item" style="left:325px;top:151px"><div class="item-title">Set daily quotas and start every day at zero</div><p class="lorem">Ipsum dolor sit amet, consectetur adipiscing elit, sed do eiusmod tempor incididunt ut labor aliqua.</p></div>
  <div class="badge" style="left:293px;top:193px;width:22px;height:24px">03</div>
  <div class="list-item" style="left:325px;top:195px"><div class="item-title">Useing app to track progress on specific goals</div><p class="lorem">Dolor sit amet, consectetur adipiscing elit, sed do eiusmod tempor incididunt ut labor aliqua.</p></div>
  <div class="badge" style="left:293px;top:243px;width:22px;height:24px">04</div>
  <div class="list-item" style="left:325px;top:245px"><div class="item-title">Track our metrics on a calendar</div><p class="lorem">Dolor sit amet, consectetur adipiscing elit, sed do eiusmod tempor incididunt ut labor aliqua.</p></div>

  <div class="footer"></div>
  <div class="footer-end" style="width:112px"><span style="right:16px">PAGE : 01</span></div>
</section>

</body>
</html>
```